Trash/recycling can & dumpster cleaning service

We power wash the inside and outside of trash/recycling cans & dumpsters. The water is collected and disposed of properly. We use environmentally safe products that leave your bins looking and smelling new.

Target Market(s)

Homeowners/renters, HOA's, Restaurant/Bars, Grocery stores, Hotel & Motels, Vacation homes, and neighborhoods with special rules to be allowed to live there.

Industry/Entity Type

Cleaning Service

Contact Information for Business Card

Bristle Bright Bins, Doug Pemberton-president-(608)555-0173, Marcus Telford-Vice President/treasurer-(608)555-0148, Madison, WI

Font styles to use
Serif

Requirements
Nice to have
• A picture of trash can (real or animated). The colors we would like to use is the same as the picture of Varo shoes in my images, sketches, or document section. Main color the aqua blue w/the bright fluorescent yellow and orange as accent colors.

```html
<!DOCTYPE html>
<html lang="en">
<head>
<meta charset="utf-8">
<title>Bristle Bright Bins – Business Cards</title>
<link href="https://fonts.googleapis.com/css2?family=Arimo:wght@400;700&display=swap" rel="stylesheet">
<style>
  :root{
    --bg:#ececec;
    --sky:#6fc4e0;
    --sky-deep:#80b0d4;
    --lavender:#e2d6ea;
    --pink:#e8649b;
    --purple:#8f4fa0;
    --stripe-lime:#b5cc35;
    --stripe-green:#56b04a;
    --stripe-purple:#9b55a0;
    --stripe-pink:#e8649b;
    --icon:#c2c03a;
    --white:#ffffff;
  }
  *{margin:0;padding:0;box-sizing:border-box}
  html,body{width:1200px;height:1000px;overflow:hidden}
  body{background:var(--bg);font-family:"Arimo",Arial,sans-serif;position:relative}

  .card{position:absolute;width:560px;height:330px;overflow:hidden;box-shadow:0 4px 14px rgba(0,0,0,.18)}
  .card--front{background:var(--sky)}
  .card--president{left:30px;top:70px}
  .card--vice{left:610px;top:70px}
  .card--back{left:320px;top:560px;width:560px;height:370px;background:var(--white)}

  .band{position:absolute;left:0;width:100%}
  .band--logo{top:45px;height:100px;background:var(--sky-deep)}
  .card--back .band--logo{top:50px;height:105px;background:var(--lavender)}

  .brand{position:absolute;left:40px;top:78px;font-weight:700;font-size:34px;color:var(--pink);letter-spacing:-.5px;display:flex;align-items:center;gap:12px}
  .brand-dot{width:16px;height:16px;border-radius:50%;background:var(--pink)}
  .card--back .brand{left:0;right:0;top:84px;justify-content:center}

  .contact{position:absolute;left:330px;top:178px;color:var(--white)}
  .contact-name{font-size:22px;font-weight:700}
  .contact-role{font-size:13px;font-weight:700;color:var(--pink);margin-top:3px}
  .contact-line{display:flex;align-items:center;gap:10px;font-size:17px;color:var(--purple);margin-top:10px}
  .contact-role + .contact-line{margin-top:18px}
  .contact-line svg{width:18px;height:18px;flex:none}

  .stripe{position:absolute;left:0;bottom:0;width:100%;height:32px;display:flex;border-top:4px solid var(--white)}
  .stripe span{flex:1}
  .stripe .lime{background:var(--stripe-lime)}
  .stripe .green{background:var(--stripe-green)}
  .stripe .purple{background:var(--stripe-purple)}
  .stripe .pink{background:var(--stripe-pink)}

  .bins-photo{position:absolute;left:0;top:200px;width:100%;height:138px;
    background:linear-gradient(90deg,#3b3b3b 0%,#4f8a3c 22%,#4a4a4a 36%,#5a6b3a 58%,#4a7fae 82%,#f4f4f4 100%)}
</style>
</head>
<body>

  <section class="card card--front card--president">
    <div class="band band--logo"></div>
    <div class="brand"><span class="brand-dot"></span>Bristle Bright Bins</div>
    <div class="contact">
      <p class="contact-name">Doug Pemberton</p>
      <p class="contact-role">President</p>
      <p class="contact-line">
        <svg viewBox="0 0 20 20" aria-hidden="true"><path fill="var(--icon)" d="M2 6c0-2 2-3 8-3s8 1 8 3v2h-4V6.5c-1-.6-7-.6-8 0V8H2zM5 9h10l2 8H3zm5 2a2 2 0 100 4 2 2 0 000-4z"/></svg>
        (608)555-0173
      </p>
      <p class="contact-line">
        <svg viewBox="0 0 20 20" aria-hidden="true"><path fill="none" stroke="var(--icon)" stroke-width="2.2" d="M10 18s-5.5-6-5.5-9.5a5.5 5.5 0 0111 0C15.5 12 10 18 10 18z"/><circle cx="10" cy="8.5" r="1.8" fill="var(--icon)"/></svg>
        Alder Falls, Chile
      </p>
    </div>
    <div class="stripe"><span class="lime"></span><span class="green"></span><span class="purple"></span><span class="pink"></span><span class="lime"></span><span class="green"></span><span class="purple"></span><span class="pink"></span></div>
  </section>

  <section class="card card--front card--vice">
    <div class="band band--logo"></div>
    <div class="brand"><span class="brand-dot"></span>Bristle Bright Bins</div>
    <div class="contact">
      <p class="contact-name">Marcus Telford</p>
      <p class="contact-role">Vice President/treasurer</p>
      <p class="contact-line">
        <svg viewBox="0 0 20 20" aria-hidden="true"><path fill="var(--icon)" d="M2 6c0-2 2-3 8-3s8 1 8 3v2h-4V6.5c-1-.6-7-.6-8 0V8H2zM5 9h10l2 8H3zm5 2a2 2 0 100 4 2 2 0 000-4z"/></svg>
        (608)555-0148
      </p>
      <p class="contact-line">
        <svg viewBox="0 0 20 20" aria-hidden="true"><path fill="none" stroke="var(--icon)" stroke-width="2.2" d="M10 18s-5.5-6-5.5-9.5a5.5 5.5 0 0111 0C15.5 12 10 18 10 18z"/><circle cx="10" cy="8.5" r="1.8" fill="var(--icon)"/></svg>
        Alder Falls, Chile
      </p>
    </div>
    <div class="stripe"><span class="lime"></span><span class="green"></span><span class="purple"></span><span class="pink"></span><span class="lime"></span><span class="green"></span><span class="purple"></span><span class="pink"></span></div>
  </section>

  <section class="card card--back">
    <div class="band band--logo"></div>
    <div class="brand"><span class="brand-dot"></span>Bristle Bright Bins</div>
    <div class="bins-photo" role="img" aria-label="Photo of wheeled trash carts and commercial dumpsters in black, green and blue"></div>
    <div class="stripe"><span class="lime"></span><span class="green"></span><span class="purple"></span><span class="pink"></span><span class="lime"></span><span class="green"></span><span class="purple"></span><span class="pink"></span></div>
  </section>

</body>
</html>
```